Client website

Our designer we were working with had some personal things come up and was unable to finish the design for the site.

We have a .psd file started, and will be attaching it to the project.

Reason: I still want to polish the designs with the current designer and allow more designers the opportunity to participate.

Reason: I'm extending the deadline for another day to give everyone enough time for the final changes our client wants.

I'm trying to extend the deadline so we can get one last set of comps in for my client.  Could everyone message me and let me know how much time they need to do the final tweaks?

Reason: Hey everyone.  I've been sick the last 3 days and I haven't been able to provide feedback on designs.  I'm extending just a few more days so I can catch up here.  Thanks everyone for your patience.

Adults in United States aged 25 to 60 that handle the household budgets and maintenance.

• 1) We need 2 pages. 1 page for flood restoration, 1 page for carpet cleaning

2) The 1-800-# must be the focal point of the website for both pages. People are mostly looking to contact someone ASAP to get them out to their house when flooding occurs.

3) We''re going to have a slide show area to high-light different sub-services offered for each page.

4) We really want a pagenest / lumora feed area. We''re going to use pagenest for special offers, and lumora for weather updates. The pagenest feed is going to be on the carpet cleaning page. The lumora feed is going to be on the flood page.

5) We want an SEO text sections near the bottom.

6) The very bottom will link to the privacy policy and user agreement as well as company name and copyright details.

We really want to stick to the say "theme" that our first designer started with.
• I'm not a designer, so if you think something looks better somewhere, or something can be eliminated, or something can be enhanced, but all means, let us know.

```html
<!DOCTYPE html>
<html lang="en">
<head>
<meta charset="utf-8">
<title>Clearwave — Water &amp; Fire Damage Restoration</title>
<link href="https://fonts.googleapis.com/css2?family=Questrial&family=Open+Sans:wght@400;600;700&display=swap" rel="stylesheet">
<style>
:root{
  --sea-top:#14b3c4;
  --sea-mid:#0b6f80;
  --sea-deep:#04262d;
  --ink:#000;
  --panel:#082a31;
  --panel-edge:#0f4a55;
  --green:#7ec21b;
  --green-dark:#2f6b08;
  --head-green:#3d7a10;
  --head-teal:#1b7f97;
  --link:#1f8fab;
  --grey-text:#8a8a8a;
  --box-light:#ececec;
  --box-mid:#d6d6d6;
  --white:#fff;
  --seo:#123f47;
  --foot:#4f8791;
}
*{margin:0;padding:0;box-sizing:border-box}
html,body{width:1200px;height:1020px;overflow:hidden;background:var(--ink)}
body{font-family:"Open Sans",Arial,sans-serif;position:relative;
  background:linear-gradient(180deg,var(--sea-top) 0,#0f95a8 120px,var(--sea-mid) 260px,var(--sea-deep) 480px,var(--ink) 640px,var(--ink) 100%)}
.glow{position:absolute;left:420px;top:-80px;width:360px;height:260px;border-radius:50%;
  background:radial-gradient(ellipse at center,rgba(220,255,255,.55),rgba(120,230,240,0) 70%)}
.brand{position:absolute;left:172px;top:60px;display:flex;align-items:center;gap:12px}
.brand-dot{width:46px;height:46px;border-radius:50%;background:#0b8fb0}
.brand-name{font-family:"Open Sans",sans-serif;font-weight:700;font-size:28px;color:#dff3f6;letter-spacing:1px}
.brand-tag{position:absolute;left:176px;top:150px;font-size:9px;color:#0a3a42;font-variant:small-caps;letter-spacing:.5px}
.contact-box{position:absolute;left:700px;top:0;width:336px;height:70px;background:linear-gradient(#063a45,#052a33);
  border:1px solid #0b4f5c;border-top:none;box-shadow:0 3px 8px rgba(0,0,0,.4)}
.phone{position:absolute;left:80px;top:5px;display:flex;align-items:center;gap:6px;
  color:var(--green);font-weight:700;font-size:19px}
.contact-rule{position:absolute;left:10px;right:10px;top:36px;border-top:1px solid #0e5462}
.social{position:absolute;right:14px;top:42px;display:flex;gap:8px;align-items:center}
.social-item{display:flex;align-items:center;gap:4px;font-size:11px;color:#cfe7ea}
.social-item span.sq{width:10px;height:10px;background:#cfe7ea;display:inline-block}
.site{position:absolute;left:130px;top:170px;width:940px;height:620px;
  background:linear-gradient(#062a31,#052129 60%,rgba(0,0,0,0));}
.nav{position:absolute;left:16px;top:18px;display:flex;gap:23px}
.nav a{color:#d8e4e6;text-decoration:none;font-weight:700;font-size:14px;letter-spacing:.5px}
.nav a.current{color:#fff;border-bottom:2px solid #bcd;padding-bottom:2px}
.nav-rule{position:absolute;left:0;right:0;top:48px;border-top:1px solid #0d4551}
.slider{position:absolute;left:16px;top:70px;width:908px;height:322px;border:1px solid var(--panel-edge);
  background:linear-gradient(180deg,#0b3b46 0,#12566a 60%,#0fb0c6 84%,#075866 90%,#031c22 100%)}
.slide-title{position:absolute;left:67px;top:100px;font-family:"Questrial",sans-serif;font-size:37px;color:#fff}
.slide-list{position:absolute;left:76px;top:146px;font-family:"Questrial",sans-serif;font-size:15px;color:#fff;list-style:none;line-height:24px}
.btn{position:absolute;left:71px;top:246px;width:145px;height:32px;background:linear-gradient(#5fc21d,#1f7d0c);
  border:1px solid #0c4a06;color:#133d06;font-family:"Questrial",sans-serif;font-size:16px;text-align:center;line-height:30px;text-decoration:none}
.slide-photo{position:absolute;left:466px;top:60px;width:327px;height:218px;border:5px solid var(--white);
  background:linear-gradient(160deg,#e9ecea,#b7b3a6 50%,#6e6a5e)}
.arrow{position:absolute;top:207px;width:48px;height:48px;border-radius:50%;background:#041a1f;border:2px solid #0d4d58;
  color:#cbd6d8;font-size:30px;text-align:center;line-height:42px;font-family:"Open Sans",sans-serif}
.arrow.prev{left:-17px}.arrow.next{left:881px}
.boxes{position:absolute;left:16px;top:404px;width:909px;height:201px;display:flex;
  background:linear-gradient(#f0f0f0,#d8d8d8);border-bottom:1px solid #bbb}
.box{position:relative;flex:0 0 auto;border-right:1px solid #c9c9c9;
  background:linear-gradient(90deg,#d2d2d2,#ebebeb 25%,#e6e6e6)}
.box:nth-child(1){width:304px}.box:nth-child(2){width:302px}.box:nth-child(3){width:303px;border-right:none}
.box-head{height:25px;border-bottom:1px solid #c6c6c6;text-align:center;font-weight:700;font-size:12px;line-height:26px;letter-spacing:.5px}
.head-green{color:var(--head-green)}.head-teal{color:var(--head-teal)}
.news{position:absolute;left:12px;top:53px;font-size:12px;color:var(--grey-text);line-height:12px;width:285px}
.news h4{color:var(--head-green);font-size:12px;font-weight:700;margin-bottom:1px}
.news p{margin-bottom:22px}
.news a{color:var(--link);text-decoration:none}
.services{position:absolute;left:17px;top:54px;list-style:none;font-size:12px;color:var(--grey-text)}
.services li{height:30px;display:flex;gap:7px}
.services li::before{content:"";width:8px;height:8px;margin-top:3px;background:#b4b4b4;border:1px solid #999}
.side-photo{position:absolute;left:54px;top:34px;width:208px;height:148px;border:5px solid var(--white);
  box-shadow:0 2px 5px rgba(0,0,0,.3);background:linear-gradient(170deg,#3fb0c8,#12677d 60%,#0b4758)}
.seo{position:absolute;left:148px;top:783px;width:904px;font-size:10.5px;line-height:12px;color:var(--seo);
  font-variant:small-caps;text-indent:18px;text-align:justify}
.foot-rule{position:absolute;left:210px;width:810px;top:890px;border-top:1px solid #0b2a30}
.foot-rule.low{top:918px}
.copy{position:absolute;left:295px;top:899px;font-size:11px;color:var(--foot)}
.legal{position:absolute;left:754px;top:899px;font-size:11px;color:var(--foot)}
.legal a{color:var(--foot);text-decoration:none}
</style>
</head>
<body>
<div class="glow"></div>

<header>
  <div class="brand"><span class="brand-dot"></span><span class="brand-name">CLEARWAVE</span></div>
  <div class="brand-tag">Water &amp; Fire Damage Restoration</div>

  <div class="contact-box">
    <div class="phone">
      <svg width="22" height="22" viewBox="0 0 24 24" aria-hidden="true"><path fill="#d9e4e6" d="M6.6 10.8c1.4 2.8 3.8 5.1 6.6 6.6l2.2-2.2c.3-.3.7-.4 1-.2 1.1.4 2.3.6 3.6.6.6 0 1 .4 1 1V20c0 .6-.4 1-1 1C10.6 21 3 13.4 3 4c0-.6.4-1 1-1h3.5c.6 0 1 .4 1 1 0 1.3.2 2.5.6 3.6.1.3 0 .7-.2 1z"/></svg>
      1-800-555-0142
    </div>
    <div class="contact-rule"></div>
    <div class="social">
      <svg width="30" height="20" viewBox="0 0 30 20" aria-label="Email"><rect x="1" y="1" width="28" height="18" fill="#e8eef0" stroke="#9aa" /><path d="M1 1l14 10L29 1" fill="none" stroke="#889"/></svg>
      <span class="social-item"><span class="sq"></span>lumora</span>
      <span class="social-item"><span class="sq"></span>pagenest</span>
    </div>
  </div>
</header>

<main class="site">
  <nav class="nav">
    <a class="current" href="#">HOME</a>
    <a href="#">ABOUT US</a>
    <a href="#">SERVICES</a>
    <a href="#">CONTACTS</a>
  </nav>
  <div class="nav-rule"></div>

  <section class="slider">
    <h2 class="slide-title">Lorem Ipsum</h2>
    <ol class="slide-list">
      <li>1. Curabitur et dui justo, vel pharetra lectus.</li>
      <li>2. Duis vel sapien at mauris egestas vestibulum.</li>
      <li>3. Nulla interdum massa urna, sed lacinia nibh.</li>
    </ol>
    <a class="btn" href="#">Learn more</a>
    <div class="slide-photo" role="img" aria-label="Photo of a flooded modern living room"></div>
    <div class="arrow prev">&lt;</div>
    <div class="arrow next">&gt;</div>
  </section>

  <section class="boxes">
    <div class="box">
      <div class="box-head head-green">NEWS &amp; EVENTS</div>
      <div class="news">
        <h4>21th May 2011</h4>
        <p>Excepteur sint occaecat cupidatat non proident, sunt in culpa qui officia deserunt mollit anim id est laborum. <a href="#">read more...</a></p>
        <h4>10th May 2011</h4>
        <p>Pint occaecat cupidatat non proident,<br>sunt in culpa est laborum. <a href="#">read more...</a></p>
      </div>
    </div>
    <div class="box">
      <div class="box-head head-teal">OUR SERVICES</div>
      <ul class="services">
        <li>Donec sed elit neque, fringilla porttitor.</li>
        <li>Nunc sed augue in ligula viverra accumsan.</li>
        <li>Curabitur non erat in mi feugiat laoreet.</li>
        <li>Pellentesque pretium tellus eu nibh tempor.</li>
      </ul>
    </div>
    <div class="box">
      <div class="box-head head-green">SPACE FOR...</div>
      <div class="side-photo" role="img" aria-label="Photo of a room filled with water"></div>
    </div>
  </section>
</main>

<p class="seo">Lorem ipsum dolor sit amet, consectetur adipisicing elit, sed do eiusmod tempor incididunt ut labore et dolore magna aliqua. Ut enim ad minim veniam, quis nostrud exercitation ullamco laboris nisi ut aliquip ex ea commodo consequat. Duis aute irure dolor in reprehenderit in voluptate velit esse cillum dolore eu fugiat nulla pariatur. Excepteur sint occaecat cupidatat non proident, sunt in culpa qui officia deserunt mollit anim id est laborum. Sed ut perspiciatis unde omnis iste natus error sit voluptatem accusantium doloremque laudantium, totam rem aperiam, eaque ipsa quae ab illo inventore veritatis et quasi architecto beatae vitae dicta sunt explicabo. Nemo enim ipsam voluptatem quia voluptas sit aspernatur aut odit aut fugit, sed quia consequuntur magni dolores eos qui ratione voluptatem sequi nesciunt. Neque porro quisquam est, qui dolorem ipsum quia dolor sit amet, consectetur, adipisci velit, sed quia non numquam eius modi tempora incidunt ut labore et dolore magnam aliquam quaerat voluptatem. Ut enim ad minima veniam, quis nostrum exercitationem ullam corporis suscipit laboriosam, nisi ut aliquid ex ea commodi consequatur? Quis autem vel eum iure reprehenderit qui in ea voluptate velit esse quam nihil molestiae consequatur, vel illum qui dolorem eum fugiat quo voluptas nulla pariatur?</p>

<footer>
  <div class="foot-rule"></div>
  <div class="copy">© 2011 CLEARWAVE. All rights reserved</div>
  <div class="legal"><a href="#">Privacy Policy</a> | <a href="#">User Agreement</a></div>
  <div class="foot-rule low"></div>
</footer>
</body>
</html>
```